Small corporate website template design

I need a couple templates designed for a small corporate website. The corporate site reflects the existence of the parent company which will own various brands/services that have their own websites, so it will mainly be used to present who we are, what we do, what is happening (news/events), how to contact us, link off to our other brand/service sites, as well as post information for public relations, investors, and job opportunities.

The company name is Velmoranth LLC (www.velmoranth-example.com), and the name is representative of stratified layers of interconnected digital services. The corporate site is not expected to generate a bunch of fanfare - that honor will be reserved for the externally linked brand/service sites.

The provided logo may be manipulated in color, size, shape, positioning, etc. to get it to fit with the design, but should be integrated in some way.

What we are looking for is a home page layout as well as a template for an inner page whereby the navigation/logo, etc may be diminished to some extent for the inner pages. We are also interested in reusable elements such as dividers, content containers, etc. in order to represent the types of information described above that we would like to present as described above.

We are particularly interested in consistency of design elements, conservative use of color (including consideration of accessibility concerns), judicious use of whitespace in favor of simplified messaging, and something lending itself well to internationalization/translation.

Target Market(s)

Small business owners, entrepreneurs (B2B)

Number of Pages Required

2 page

Font styles to use
Sans Serif

Requirements
Must have
• See the attached PDF with the logo concept, color swatches, and comparative sites.

```html
<!DOCTYPE html>
<html lang="en">
<head>
<meta charset="utf-8">
<title>Velmoranth LLC — Strategic Design and Technology Agency</title>
<link href="https://fonts.googleapis.com/css2?family=Jost:wght@400;500;600&display=swap" rel="stylesheet">
<style>
:root{
  --navy:#14305f;
  --blue:#2c5a97;
  --blue-soft:#6596d3;
  --orange:#f4a01c;
  --text:#3a4150;
  --muted:#8a909c;
  --tint:#f0f4fc;
  --white:#ffffff;
  --line:#e3e8f1;
}
*{box-sizing:border-box;margin:0;padding:0}
html,body{width:1200px;height:3209px;overflow:hidden}
body{position:relative;background:var(--white);font-family:'Jost',sans-serif;color:var(--text)}
.abs{position:absolute}
.bg-shape{position:absolute;left:0;top:0}
.site-header{position:absolute;left:0;top:0;width:1200px;height:100px;z-index:10}
.btn{position:absolute;display:flex;align-items:center;justify-content:center;border-radius:20px;color:var(--white);font-size:10px;font-weight:500;letter-spacing:1.2px;text-transform:uppercase;box-shadow:0 6px 14px rgba(44,90,151,.25)}
.btn--dark{background:var(--blue)}
.btn--soft{background:var(--blue-soft)}
.brand{position:absolute;display:flex;align-items:center;gap:9px;font-size:21px;font-weight:600;color:var(--navy)}
.brand__dot{width:20px;height:20px;border-radius:50%;background:var(--navy)}
.nav{position:absolute;top:40px;left:428px;width:400px;height:20px;font-size:14px}
.nav a{position:absolute;top:0;white-space:nowrap;color:#333;text-decoration:none}
.nav a.is-active{color:var(--orange)}
.eyebrow{position:absolute;font-size:16px;color:var(--orange)}
.h-section{position:absolute;font-size:28px;font-weight:500;line-height:1.28;color:var(--navy)}
.photo{position:absolute;border-radius:14px}
.card{position:absolute;background:var(--white);box-shadow:0 8px 26px rgba(30,50,90,.09);border-radius:3px}
.service__icon{position:absolute;left:24px;top:28px}
.service__title{position:absolute;left:106px;top:26px;font-size:14px;font-weight:500;color:#1d2433;letter-spacing:.4px}
.service__title.is-link{color:var(--blue-soft);text-decoration:underline}
.service__text{position:absolute;left:106px;top:50px;width:310px;font-size:11px;line-height:1.5;color:var(--muted)}
.feature__title{position:absolute;font-size:14px;font-weight:500;color:#1d2433;letter-spacing:.4px}
.post__cat{position:absolute;font-size:11px;letter-spacing:1px;color:var(--blue-soft);text-transform:uppercase}
.post__title{position:absolute;width:293px;font-size:13px;font-weight:500;line-height:1.35;color:#1d2433}
.post__title.is-link{text-decoration:underline}
.post__date{position:absolute;font-size:11px;letter-spacing:1px;color:var(--muted)}
.footer__head{position:absolute;font-size:14px;font-weight:500;color:#1d2433;letter-spacing:.4px}
.footer__links{position:absolute;list-style:none;font-size:13px;line-height:30px;color:var(--muted)}
.footer__links .is-active{color:var(--blue-soft)}
.social{position:absolute;width:30px;height:30px;border-radius:50%;border:1px solid var(--line);background:var(--white)}
</style>
</head>
<body>

<!-- soft background shapes -->
<svg class="bg-shape" width="1200" height="3209" viewBox="0 0 1200 3209" aria-hidden="true">
  <path d="M0 820 C180 800 300 900 380 1010 C450 1110 470 1260 560 1380 C380 1440 160 1420 0 1470 Z" fill="var(--tint)"/>
  <path d="M0 1190 C220 1250 420 1290 520 1440 C420 1500 200 1520 0 1500 Z" fill="#f6f8fd"/>
  <path d="M1200 1990 C1060 2000 960 2120 930 2300 C900 2520 980 2760 1200 2860 Z" fill="var(--tint)"/>
</svg>

<!-- hero image area -->
<svg class="abs" style="left:0;top:0" width="1200" height="710" viewBox="0 0 1200 710" role="img" aria-label="Photo of a team meeting around an office table with a presenter standing">
  <defs>
    <linearGradient id="heroTone" x1="0" y1="0" x2="1" y2="1">
      <stop offset="0" stop-color="#e9ecef"/>
      <stop offset=".5" stop-color="#c9b9a8"/>
      <stop offset="1" stop-color="#6f7f95"/>
    </linearGradient>
  </defs>
  <path d="M470 0 C400 70 370 180 470 300 C600 450 900 640 1200 706 L1200 0 Z" fill="url(#heroTone)"/>
</svg>

<!-- header -->
<header class="site-header">
  <div class="brand" style="left:135px;top:36px"><span class="brand__dot"></span>Velmoranth</div>
  <nav class="nav">
    <a class="is-active" style="left:0">Home</a>
    <a style="left:75px">About</a>
    <a style="left:152px">Services</a>
    <a style="left:244px">Blog</a>
    <a style="left:310px">Contact</a>
  </nav>
  <div class="btn btn--dark" style="left:898px;top:28px;width:165px;height:43px">Start a Project</div>
</header>

<!-- hero -->
<h1 class="abs" style="left:135px;top:265px;font-size:30px;font-weight:500;line-height:1.25;color:var(--navy)">Strategic Design<br>and Technology Agency.</h1>
<p class="abs" style="left:135px;top:352px;font-size:16px;color:#333">Designed to serve your business.</p>
<div class="btn btn--soft" style="left:135px;top:406px;width:132px;height:33px">Contact Us</div>
<svg class="abs" style="left:592px;top:612px" width="14" height="18" viewBox="0 0 14 18" aria-hidden="true"><path d="M7 1 V16 M2 11 L7 16 L12 11" fill="none" stroke="var(--orange)" stroke-width="1.6"/></svg>

<!-- about -->
<div class="abs" style="left:160px;top:712px;width:291px;height:343px;border:2px solid var(--blue-soft);border-radius:3px"></div>
<div class="photo" role="img" aria-label="Photo of three colleagues smiling at a tablet" style="left:135px;top:738px;width:293px;height:342px;background:linear-gradient(135deg,#d8cbbd,#8e9bb0)"></div>
<div class="eyebrow" style="left:507px;top:745px">About Velmoranth</div>
<h2 class="h-section" style="left:507px;top:782px;width:385px">There are many variations of passages of Lorem Ipsum available</h2>
<div class="abs" style="left:507px;top:933px;width:54px;height:1px;background:var(--orange)"></div>
<p class="abs" style="left:588px;top:922px;width:480px;font-size:11px;line-height:1.7;color:var(--muted)">Contrary to popular belief, Lorem Ipsum is not simply random text.<br>It has roots in a piece of classical Latin literature from 45 BC, making it over<br>2000 years old. Richard McClintock, a Latin professor ...</p>
<div class="btn btn--dark" style="left:588px;top:1016px;width:133px;height:33px">Discover More</div>

<!-- services -->
<div class="eyebrow" style="left:0;width:1200px;text-align:center;top:1163px">What We Do</div>
<h2 class="h-section" style="left:0;width:1200px;text-align:center;top:1190px">Our Best Services</h2>

<div class="card" style="left:135px;top:1253px;width:451px;height:122px">
  <svg class="service__icon" width="56" height="56" viewBox="0 0 56 56" aria-hidden="true"><rect x="6" y="8" width="44" height="30" rx="2" fill="none" stroke="var(--blue)" stroke-width="2"/><rect x="14" y="15" width="12" height="16" fill="none" stroke="var(--blue)" stroke-width="1.6"/><path d="M30 17 H43 M30 23 H43 M30 29 H39 M22 46 H34 M28 38 V46" stroke="var(--blue)" stroke-width="1.6"/></svg>
  <div class="service__title">Creative Websites</div>
  <p class="service__text">It is a long established fact that a reader will be distracted by the readable content of a page when looking at its layout.</p>
</div>
<div class="card" style="left:612px;top:1253px;width:451px;height:122px">
  <svg class="service__icon" width="56" height="56" viewBox="0 0 56 56" aria-hidden="true"><rect x="6" y="8" width="44" height="30" rx="2" fill="none" stroke="var(--orange)" stroke-width="2"/><circle cx="28" cy="23" r="7" fill="none" stroke="var(--orange)" stroke-width="1.6"/><path d="M22 46 H34 M28 38 V46" stroke="var(--orange)" stroke-width="1.6"/></svg>
  <div class="service__title is-link">UX&amp;UI Design</div>
  <p class="service__text">It is a long established fact that a reader will be distracted by the readable content of a page when looking at its layout.</p>
</div>
<div class="card" style="left:135px;top:1403px;width:451px;height:124px">
  <svg class="service__icon" width="56" height="56" viewBox="0 0 56 56" aria-hidden="true"><rect x="8" y="8" width="40" height="32" rx="2" fill="none" stroke="var(--blue)" stroke-width="2"/><path d="M8 15 H48 M23 24 L19 28 L23 32 M33 24 L37 28 L33 32 M4 46 H52" fill="none" stroke="var(--blue)" stroke-width="1.6"/></svg>
  <div class="service__title">Development</div>
  <p class="service__text">It is a long established fact that a reader will be distracted by the readable content of a page when looking at its layout.</p>
</div>
<div class="card" style="left:612px;top:1403px;width:451px;height:124px">
  <svg class="service__icon" width="56" height="56" viewBox="0 0 56 56" aria-hidden="true"><circle cx="22" cy="30" r="10" fill="none" stroke="var(--blue)" stroke-width="2"/><circle cx="22" cy="30" r="4" fill="none" stroke="var(--blue)" stroke-width="1.6"/><circle cx="38" cy="16" r="7" fill="none" stroke="var(--blue)" stroke-width="1.6"/><circle cx="38" cy="16" r="2.5" fill="none" stroke="var(--blue)" stroke-width="1.4"/></svg>
  <div class="service__title">Custom Solutions</div>
  <p class="service__text">It is a long established fact that a reader will be distracted by the readable content of a page when looking at its layout.</p>
</div>
<div class="btn btn--soft" style="left:533px;top:1572px;width:134px;height:33px">Contact Us</div>

<!-- why choose -->
<div class="eyebrow" style="left:135px;top:1790px">Why Choose Velmoranth</div>
<h2 class="h-section" style="left:135px;top:1823px;width:330px;font-size:24px">There are many variations of passages of Lorem Ipsum site available</h2>
<div class="btn btn--dark" style="left:135px;top:1946px;width:133px;height:33px">Get Started</div>

<div class="card" style="left:667px;top:1690px;width:343px;height:113px">
  <svg class="abs" style="left:26px;top:26px" width="52" height="52" viewBox="0 0 52 52" aria-hidden="true"><circle cx="26" cy="26" r="26" fill="var(--tint)"/><rect x="17" y="19" width="15" height="11" rx="1" fill="none" stroke="var(--blue)" stroke-width="1.4"/><rect x="31" y="22" width="5" height="10" rx="1" fill="none" stroke="var(--blue)" stroke-width="1.4"/></svg>
  <div class="feature__title" style="left:104px;top:44px">Responsive Design</div>
</div>
<div class="card" style="left:667px;top:1968px;width:343px;height:117px">
  <svg class="abs" style="left:26px;top:32px" width="52" height="52" viewBox="0 0 52 52" aria-hidden="true"><circle cx="26" cy="26" r="26" fill="var(--tint)"/><text x="26" y="32" text-anchor="middle" font-family="Jost,sans-serif" font-size="17" fill="var(--blue)">$</text></svg>
  <div class="feature__title" style="left:104px;top:50px">Affordable Pricing</div>
</div>
<div class="card" style="left:612px;top:1803px;width:451px;height:165px;box-shadow:0 12px 34px rgba(30,50,90,.14)">
  <svg class="abs" style="left:26px;top:28px" width="110" height="110" viewBox="0 0 110 110" aria-hidden="true"><circle cx="55" cy="55" r="55" fill="var(--blue-soft)"/><path d="M38 60 V52 A17 17 0 0 1 72 52 V60" fill="none" stroke="var(--white)" stroke-width="3.5"/><rect x="33" y="55" width="10" height="16" rx="3" fill="var(--white)"/><rect x="67" y="55" width="10" height="16" rx="3" fill="var(--white)"/></svg>
  <div class="feature__title" style="left:160px;top:44px">Great Customer Support</div>
  <p class="abs" style="left:160px;top:68px;width:270px;font-size:11px;line-height:1.5;color:var(--muted)">Lorem ipsum dolor sit, adipiscing elit, sed do eiusmod tempor ut labore et dolore site amet ...</p>
</div>

<!-- news -->
<div class="photo" role="img" aria-label="Photo of colleagues working together at a laptop" style="left:135px;top:2169px;width:293px;height:182px;border-radius:3px;background:linear-gradient(135deg,#c9d3dc,#9aa7b3)"></div>
<div class="photo" role="img" aria-label="Photo of people working at desks in a creative office" style="left:453px;top:2169px;width:293px;height:182px;border-radius:3px;background:linear-gradient(135deg,#c98a6e,#7c6a62)"></div>
<div class="photo" role="img" aria-label="Photo of a designer sketching wireframes at a desk" style="left:772px;top:2169px;width:293px;height:182px;border-radius:3px;background:linear-gradient(135deg,#3f8fa0,#2b4d62)"></div>

<div class="post__cat" style="left:135px;top:2374px">News</div>
<div class="post__title" style="left:135px;top:2398px">There are many variations passages<br>of Lorem Ipsum site</div>
<div class="post__date" style="left:135px;top:2449px">25-March-2018</div>

<div class="post__cat" style="left:453px;top:2374px">Blog</div>
<div class="post__title is-link" style="left:453px;top:2398px">There are many variations passages<br>of Lorem Ipsum site</div>
<div class="post__date" style="left:453px;top:2449px">30-March-2018</div>

<div class="post__cat" style="left:772px;top:2374px">News</div>
<div class="post__title" style="left:772px;top:2398px">There are many variations passages<br>of Lorem Ipsum site</div>
<div class="post__date" style="left:772px;top:2449px">22-April-2018</div>

<!-- careers band -->
<section class="abs" style="left:135px;top:2548px;width:930px;height:250px;background:var(--blue);border-radius:2px">
  <p class="abs" style="left:0;width:930px;top:56px;text-align:center;font-size:24px;color:var(--white)">Take your career to next level. join our team &amp; see</p>
  <p class="abs" style="left:0;width:930px;top:90px;text-align:center;font-size:30px;font-weight:500;color:var(--orange)">what we can do together.</p>
  <div class="btn btn--soft" style="left:398px;top:156px;width:134px;height:34px">Join the Team</div>
</section>

<!-- footer -->
<div class="brand" style="left:135px;top:2897px"><span class="brand__dot"></span>Velmoranth</div>
<p class="abs" style="left:135px;top:2940px;font-size:13px;color:#333">info@velmoranth-example.com</p>
<p class="abs" style="left:135px;top:2960px;font-size:14px;color:var(--blue-soft)">555-010-2040</p>

<div class="footer__head" style="left:400px;top:2880px">Browse Website</div>
<ul class="footer__links" style="left:400px;top:2903px"><li>About Us</li><li class="is-active">Blog</li><li>Testimonials</li><li>Contact Us</li></ul>

<div class="footer__head" style="left:637px;top:2880px">Services</div>
<ul class="footer__links" style="left:637px;top:2903px"><li>Creative Websites</li><li>UX&amp;UI Design</li><li>Development</li><li>Custom Solutions</li></ul>

<div class="footer__head" style="left:851px;top:2880px">Subscribe Us</div>
<div class="abs" style="left:851px;top:2913px;width:214px;height:40px;border:1px solid var(--line);background:var(--white);font-size:11px;color:var(--muted);padding:12px 14px">Your email ...</div>
<svg class="abs" style="left:1040px;top:2926px" width="14" height="14" viewBox="0 0 14 14" aria-hidden="true"><path d="M1 7 H12 M8 3 L12 7 L8 11" fill="none" stroke="#333" stroke-width="1.3"/></svg>
<span class="social" style="left:851px;top:2980px"></span>
<span class="social" style="left:893px;top:2980px"></span>
<span class="social" style="left:935px;top:2980px"></span>

<p class="abs" style="left:0;width:1200px;top:3104px;text-align:center;font-size:12px;letter-spacing:1px;color:var(--muted)">© 2018 <span style="color:var(--navy);font-weight:500">Velmoranth</span>. All rights reserved.</p>
<svg class="abs" style="left:1132px;top:3086px" width="26" height="26" viewBox="0 0 26 26" aria-hidden="true"><circle cx="13" cy="13" r="13" fill="var(--orange)"/><path d="M8 15 L13 10 L18 15" fill="none" stroke="var(--white)" stroke-width="2"/></svg>

</body>
</html>
```